Business card for massage therapy company called Blue Fern Wellness

Need business card for massage therapy company called Blue Fern Wellness. Would like my logo on the front and the back of the card I have 3 options of logos and you can play with what looks better.

Would like this information displayed on the back of the card:

Marcus Ellery
Licensed Massage Therapist
415-903-2264
bluefern-wellness.example
bluefern_wellness_

```html
<!DOCTYPE html>
<html lang="en">
<head>
<meta charset="utf-8">
<title>Blue Fern Wellness – Business Card</title>
<link rel="stylesheet" href="https://fonts.googleapis.com/css2?family=Montserrat:wght@500;700&display=swap">
<style>
  :root {
    --backdrop: #3d3d3f;
    --card-white: #ffffff;
    --sage: #687055;
    --sage-dark: #4f5a3c;
    --tan: #c39672;
    --ink: #1c1c1c;
  }
  * { box-sizing: border-box; margin: 0; padding: 0; }
  html, body {
    width: 1200px; height: 1200px; overflow: hidden;
    background: var(--backdrop);
  }
  .stage {
    width: 1200px; height: 1200px;
    display: flex; flex-direction: column; align-items: center; justify-content: center;
    gap: 56px;
  }
  .card {
    position: relative;
    width: 900px; height: 514px;
    border-radius: 36px;
    overflow: hidden;
  }
  /* Front: contact side */
  .card--front { background: var(--card-white); }
  .contact {
    position: absolute; left: 64px; top: 170px;
    font-family: "Montserrat", sans-serif;
    color: var(--ink);
  }
  .contact__name {
    font-weight: 700; font-size: 40px; letter-spacing: 0.5px;
    color: var(--sage); text-transform: uppercase; line-height: 1;
  }
  .contact__title {
    font-weight: 500; font-size: 22px; margin-top: 6px; margin-bottom: 22px;
  }
  .contact__list { list-style: none; }
  .contact__item {
    display: flex; align-items: center; gap: 12px;
    font-weight: 500; font-size: 27px; line-height: 1; margin-bottom: 16px;
  }
  .contact__icon { width: 28px; height: 28px; flex: none; }
  .brand {
    display: flex; align-items: center; gap: 14px;
    font-family: "Montserrat", sans-serif; font-weight: 500;
    white-space: nowrap; line-height: 1;
  }
  .brand__dot {
    flex: none; border-radius: 50%; background: currentColor;
  }
  .card--front .brand {
    position: absolute; right: 56px; top: 84px;
    font-size: 28px; color: var(--sage);
  }
  .card--front .brand__dot { width: 30px; height: 30px; }
  .front-bands { position: absolute; left: 0; bottom: 0; width: 900px; height: 80px; }
  /* Back: logo side */
  .card--back {
    background: var(--sage);
    display: flex; align-items: center; justify-content: center;
  }
  .card--back .brand { font-size: 54px; color: var(--card-white); gap: 22px; }
  .card--back .brand__dot { width: 56px; height: 56px; }
</style>
</head>
<body>
<main class="stage">
  <section class="card card--front" aria-label="Card front">
    <div class="brand">
      <span class="brand__dot" aria-hidden="true"></span>
      <span class="brand__name">Blue Fern Wellness</span>
    </div>
    <div class="contact">
      <h1 class="contact__name">Marcus Ellery</h1>
      <p class="contact__title">Licensed Massage Therapist</p>
      <ul class="contact__list">
        <li class="contact__item">
          <svg class="contact__icon" viewBox="0 0 24 24" aria-hidden="true"><path fill="#4f5a3c" d="M6.6 10.8a15.1 15.1 0 0 0 6.6 6.6l2.2-2.2a1 1 0 0 1 1-.25 11.4 11.4 0 0 0 3.6.57 1 1 0 0 1 1 1V20a1 1 0 0 1-1 1A17 17 0 0 1 3 4a1 1 0 0 1 1-1h3.5a1 1 0 0 1 1 1c0 1.25.2 2.45.57 3.57a1 1 0 0 1-.25 1z"/></svg>
          415-903-2264
        </li>
        <li class="contact__item">
          <svg class="contact__icon" viewBox="0 0 24 24" aria-hidden="true"><rect x="3" y="3" width="18" height="18" rx="4" fill="none" stroke="#4f5a3c" stroke-width="2"/></svg>
          @bluefern_wellness_
        </li>
        <li class="contact__item">
          <svg class="contact__icon" viewBox="0 0 24 24" aria-hidden="true"><g fill="none" stroke="#4f5a3c" stroke-width="1.8"><circle cx="12" cy="12" r="9.5"/><ellipse cx="12" cy="12" rx="4.2" ry="9.5"/><path d="M2.5 12h19M4 7h16M4 17h16"/></g></svg>
          bluefern-wellness.example
        </li>
      </ul>
    </div>
    <svg class="front-bands" viewBox="0 0 900 80" aria-hidden="true">
      <polygon points="0,44 520,44 490,80 0,80" fill="var(--sage)"/>
      <polygon points="552,0 900,0 900,80 510,80" fill="var(--tan)"/>
    </svg>
  </section>

  <section class="card card--back" aria-label="Card back">
    <div class="brand">
      <span class="brand__dot" aria-hidden="true"></span>
      <span class="brand__name">Blue Fern Wellness</span>
    </div>
  </section>
</main>
</body>
</html>
```